Need Business Cards for my Business

email address: rkpmarlowhollowworks@vendrimail.com
web address: rkpmarlowhollowworks.net
Slogan: We offer various QVN licenses
Rowland K. Pemberly
Please stick with colors of Company Logo
would like the card to be more of the color example of the logo.
If you need PDF copy of logo email me at the above account.
Creative control rests with you.

Industry/Entity Type

Business

Contact Information for Business Card

I am a minimalist, but would like something to pop and stand out amongst other cards, make it memorable.

Font styles to use
Serif
Decorative
Script

```html
<!DOCTYPE html>
<html lang="en">
<head>
<meta charset="utf-8">
<title>RKP Marlow Hollow Works – Business Cards</title>
<link href="https://fonts.googleapis.com/css2?family=Open+Sans:wght@400;600;700&display=swap" rel="stylesheet">
<style>
  :root {
    --backdrop: #3a3b3d;
    --brand-blue: #1f4f9a;
    --brand-blue-light: #2f6fc0;
    --brand-blue-dark: #173d7a;
    --brand-red: #d8232a;
    --ink: #1c1c1c;
    --paper: #ffffff;
  }
  * { margin: 0; padding: 0; box-sizing: border-box; }
  html, body {
    width: 1200px; height: 900px; overflow: hidden;
    background: var(--backdrop);
    font-family: "Open Sans", Arial, sans-serif;
  }
  .stage { position: relative; width: 1200px; height: 900px; }
  .card {
    position: absolute; width: 680px; height: 388px;
    border-radius: 4px; overflow: hidden;
    box-shadow: 0 14px 30px rgba(0,0,0,.45);
  }

  /* Back of card */
  .card-back {
    left: 440px; top: 60px;
    background: radial-gradient(circle at 45% 35%, var(--brand-blue-light), var(--brand-blue) 55%, var(--brand-blue-dark));
    color: var(--paper);
  }
  .card-back .brand {
    position: absolute; left: 0; right: 0; top: 130px;
    display: flex; align-items: center; justify-content: center; gap: 16px;
  }
  .brand-dot {
    width: 26px; height: 26px; border-radius: 50%;
  }
  .card-back .brand-dot { background: var(--paper); }
  .brand-name {
    font-weight: 700; font-size: 34px; letter-spacing: 1px; text-transform: uppercase;
  }
  .slogan {
    position: absolute; left: 0; right: 0; top: 250px;
    text-align: center; font-size: 19px; letter-spacing: 1px; font-weight: 400;
  }

  /* Front of card */
  .card-front { left: 80px; top: 440px; background: var(--paper); color: var(--ink); }
  .card-front .brand {
    position: absolute; left: 42px; top: 44px;
    display: flex; align-items: center; gap: 12px; color: var(--brand-blue);
  }
  .card-front .brand-dot { background: var(--brand-red); width: 22px; height: 22px; }
  .card-front .brand-name { font-size: 27px; }
  .person { position: absolute; left: 42px; top: 118px; }
  .person-name { font-size: 25px; font-weight: 400; }
  .person-role { font-size: 17px; color: var(--brand-blue-light); margin-top: 2px; }
  .contacts { position: absolute; left: 42px; top: 196px; list-style: none; font-size: 17px; }
  .contacts li { display: flex; align-items: center; gap: 12px; margin-bottom: 8px; }
  .contacts svg { width: 16px; height: 16px; fill: var(--brand-blue); flex: none; }
  .swoosh { position: absolute; left: 0; bottom: 0; width: 680px; height: 388px; }
  .website {
    position: absolute; right: 34px; bottom: 18px;
    color: var(--paper); font-size: 19px; letter-spacing: .5px;
  }
</style>
</head>
<body>
<main class="stage">

  <section class="card card-back" aria-label="Back of business card">
    <div class="brand">
      <span class="brand-dot"></span>
      <span class="brand-name">RKP Marlow Hollow Works</span>
    </div>
    <p class="slogan">We offer various QVN licenses</p>
  </section>

  <section class="card card-front" aria-label="Front of business card">
    <svg class="swoosh" viewBox="0 0 680 388" aria-hidden="true">
      <path d="M0,268 C220,282 470,352 680,318 L680,388 L0,388 Z" fill="var(--brand-blue)"/>
      <path d="M0,262 C220,276 470,346 680,310" fill="none" stroke="var(--paper)" stroke-width="6"/>
      <path d="M60,262 C250,276 470,336 680,298" fill="none" stroke="var(--brand-red)" stroke-width="6"/>
    </svg>

    <div class="brand">
      <span class="brand-dot"></span>
      <span class="brand-name">RKP Marlow Hollow Works</span>
    </div>

    <div class="person">
      <p class="person-name">Rowland K. Pemberly</p>
      <p class="person-role">Manager</p>
    </div>

    <ul class="contacts">
      <li>
        <svg viewBox="0 0 24 24"><path d="M6.6 10.8a15.1 15.1 0 0 0 6.6 6.6l2.2-2.2a1 1 0 0 1 1-.25 11.4 11.4 0 0 0 3.6.57 1 1 0 0 1 1 1V20a1 1 0 0 1-1 1A17 17 0 0 1 3 4a1 1 0 0 1 1-1h3.5a1 1 0 0 1 1 1c0 1.25.2 2.45.57 3.57a1 1 0 0 1-.25 1z"/></svg>
        555-014-2871
      </li>
      <li>
        <svg viewBox="0 0 24 24"><path d="M2 5h20v14H2z M3 6l9 7 9-7" fill="var(--brand-blue)"/><path d="M3 6.5l9 6.5 9-6.5" fill="none" stroke="#fff" stroke-width="1.6"/></svg>
        rkpmarlowhollowworks@vendrimail.com
      </li>
    </ul>

    <p class="website">www.rkpmarlowhollowworks.net</p>
  </section>

</main>
</body>
</html>
```